online jewellery store business card

all black business card, glossy, with gold writing, gold logo and name (provided). simple design.

Target Market(s)

This business card is to put with purchases, so it just needs the logo and name Velmora Jewellery which I have uploaded pictures for you to use. Then it needs the web address, bidlorn address, email address and then the like us on KL for 10% off. All words to be used have been provided. Thanks

Industry/Entity Type

Store

Contact Information for Business Card

www.velmorajewellery.com
stores.bidlorn.com.au/Velmora-Jewellery
info@velmorajewellery.com

Like us on kinloop for 10% off your next purchase!

Requirements
Must have
• black background
gold writing
glossy look
Should not have
• yellow writing

```html
<!DOCTYPE html>
<html lang="en">
<head>
<meta charset="utf-8">
<title>Velmora Jewellery – Business Card</title>
<link href="https://fonts.googleapis.com/css2?family=Montserrat:wght@400;500;700&display=swap" rel="stylesheet">
<style>
  :root {
    --backdrop: #2a2a2c;
    --card: #0b0e17;
    --gold: #c9a75e;
    --gold-soft: #b8975a;
  }
  * { box-sizing: border-box; margin: 0; padding: 0; }
  html, body { width: 1200px; height: 900px; overflow: hidden; }
  body {
    background: var(--backdrop);
    font-family: "Montserrat", Arial, sans-serif;
    color: var(--gold);
    position: relative;
  }
  .card {
    position: absolute;
    left: 290px;
    width: 620px;
    height: 354px;
    background: linear-gradient(135deg, #121726 0%, var(--card) 55%, #07090f 100%);
    border-radius: 4px;
    box-shadow: 0 10px 30px rgba(0,0,0,.45);
  }
  .card--front { top: 70px; }
  .card--back { top: 476px; }

  .brand-mark {
    width: 96px; height: 96px;
    border: 2px solid var(--gold-soft);
    border-radius: 50%;
  }
  .brand-name {
    font-weight: 500;
    letter-spacing: .2em;
    text-transform: uppercase;
    line-height: 1.2;
    color: var(--gold);
  }

  .card--front .front-lockup {
    position: absolute; inset: 0;
    display: flex; flex-direction: column; align-items: center; justify-content: center;
    gap: 20px;
  }
  .card--front .brand-name { font-size: 30px; text-align: center; }

  .card--back .brand-mark { position: absolute; left: 44px; top: 60px; width: 130px; height: 130px; }
  .card--back .brand-name { position: absolute; left: 196px; top: 66px; font-size: 28px; }
  .contact-list {
    position: absolute; left: 228px; top: 150px;
    list-style: none;
    font-size: 15px; line-height: 1.55;
    color: var(--gold-soft);
  }
  .social-offer {
    position: absolute; left: 160px; top: 262px;
    display: flex; align-items: center; gap: 16px;
  }
  .social-square {
    width: 50px; height: 50px;
    background: var(--gold);
    border-radius: 3px;
  }
  .social-offer p { font-size: 21px; line-height: 1.2; color: var(--gold); }
  .social-offer strong { font-weight: 700; }
</style>
</head>
<body>
  <section class="card card--front" aria-label="Card front">
    <div class="front-lockup">
      <div class="brand-mark"></div>
      <h1 class="brand-name">Velmora<br>Jewellery</h1>
    </div>
  </section>

  <section class="card card--back" aria-label="Card back">
    <div class="brand-mark"></div>
    <h2 class="brand-name">Velmora<br>Jewellery</h2>
    <ul class="contact-list">
      <li>www.velmorajewellery.com</li>
      <li>stores.bidlorn.com.au/Velmora-Jewellery</li>
      <li>info@velmorajewellery.com</li>
    </ul>
    <div class="social-offer">
      <div class="social-square"></div>
      <p>Like us on kinloop<br><strong>for 10% off</strong> your next purchase!</p>
    </div>
  </section>
</body>
</html>
```